Velmi Corporate Website for technological company

We need a modern website to promote our product and services.
You can found the actually website at the address: www.velmi-example.ch

We are a new company for B2B market. We would like do show our high precision and innovation capability.

we need a section were is possible to easily upload "news" and documents for our customers.

Target Market(s)

B2B services in the industry market

Industry/Entity Type

It Company

Coding

Coded - Design and coding required

Number of Pages Required

5+ page

Font styles to use
Other font styles liked:
• We accept propositions

Requirements
Must have
• Easy to maintain
• Presentation of the Velmi company
• Presentation of Velmi services and products
• The customer can download our ducumentation
Nice to have
• Sexy and modern

```html
<!DOCTYPE html>
<html lang="en">
<head>
<meta charset="utf-8">
<title>Velmi Sàrl – Electronic & Mechanical Design</title>
<link rel="stylesheet" href="https://fonts.googleapis.com/css2?family=Krona+One&family=Open+Sans:wght@400;600;700;800&display=swap">
<style>
:root{
  --olive:#a59a4c;
  --olive-dark:#8c8240;
  --gold:#d9c862;
  --ink:#1f1f1f;
  --dark:#242424;
  --grey:#efefef;
  --text:#444;
  --muted:#777;
  --white:#fff;
  --sale:#d0121b;
  --star:#f2a516;
}
*{box-sizing:border-box;margin:0;padding:0}
html,body{width:1200px;height:3267px;overflow:hidden}
body{font-family:"Open Sans",Arial,sans-serif;color:var(--text);background:var(--white);position:relative}
a{text-decoration:none}
.abs{position:absolute}
svg{display:block}

/* header */
.topbar{left:0;top:0;width:1200px;height:115px}
.brand{left:61px;top:42px;display:flex;align-items:center;gap:12px;font-weight:800;font-size:38px;color:var(--ink);letter-spacing:1px}
.brand .mark{width:34px;height:34px;background:var(--olive)}
.callus{left:767px;top:16px;font-size:14px;font-weight:600;color:var(--ink);display:flex;align-items:center;gap:10px}
.social{left:1045px;top:12px;display:flex;gap:6px}
.social span{width:24px;height:24px;border-radius:50%;background:var(--ink)}
.search{left:466px;top:61px;width:536px;height:38px;border:2px solid var(--olive);display:flex}
.search .field{flex:1;padding:8px 12px;font-size:14px;color:#999}
.search .cat{width:212px;border-left:1px solid #ccc;padding:8px 12px;font-size:14px;color:#999;position:relative}
.search .cat:after{content:"";position:absolute;right:14px;top:14px;border:6px solid transparent;border-top-color:#444}
.search .go{width:44px;background:var(--olive);display:flex;align-items:center;justify-content:center}
.cart{left:1024px;top:64px;display:flex;align-items:center;gap:8px;font-size:17px;font-weight:600;color:var(--ink)}
.cart .count{position:absolute;left:100px;top:-10px;width:22px;height:22px;border-radius:50%;background:var(--olive);color:var(--white);font-size:12px;text-align:center;line-height:22px}

.nav{left:0;top:115px;width:1200px;height:44px;background:var(--olive)}
.nav a{position:absolute;top:0;height:44px;line-height:44px;color:var(--white);font-weight:700;font-size:15px;text-transform:uppercase}
.nav a.active{background:var(--ink);padding:0 10px}

/* hero */
.hero{left:0;top:159px;width:1200px;height:566px;background:linear-gradient(100deg,#cfd3d6 0%,#6f7478 25%,#2f2f30 45%,#4a4744 60%,#1c1c1c 85%,#3b3f45 100%)}
.hero-title{left:250px;top:338px;width:697px;height:130px;background:rgba(20,20,20,.82);text-align:center;padding-top:24px}
.hero-title .l1{color:var(--gold);font-size:33px;font-weight:600;letter-spacing:.5px}
.hero-title .l2{color:var(--white);font-size:33px;font-weight:400;letter-spacing:.5px}

/* promo banners */
.promo{left:0;top:725px;width:1200px;height:172px}
.promo .bg{left:0;top:0}
.promo h3{position:absolute;color:var(--white);font-size:21px;font-weight:700;text-transform:uppercase}
.promo p{position:absolute;color:var(--white);font-size:13px;line-height:22px;width:385px}

/* welcome */
.welcome-title{left:0;top:1000px;width:1200px;display:flex;justify-content:center;align-items:center;gap:16px;font-family:"Krona One",sans-serif;font-size:38px;font-weight:400;color:var(--ink)}
.welcome-title .name{color:var(--olive)}
.intro{left:160px;top:1080px;width:880px;text-align:center;font-size:13px;line-height:26px;color:var(--ink)}
.feature{width:280px;text-align:center}
.feature svg{margin:0 auto}
.feature h4{margin-top:44px;font-size:15px;font-weight:700;color:var(--ink);text-transform:uppercase}
.feature p{width:226px;margin:14px auto 0;font-size:13px;line-height:25px;color:var(--ink)}
.btn{display:inline-block;background:var(--olive);color:var(--white);font-weight:700;border:2px solid var(--ink);box-shadow:inset 0 0 0 2px var(--olive),inset 0 0 0 3px var(--white)}
.btn-services{left:500px;top:1544px;width:222px;height:46px;line-height:42px;text-align:center;font-size:19px}

/* why */
.why{left:0;top:1673px;width:1200px;height:461px;background:radial-gradient(circle at 45% 50%,#5a4b34 0%,#2e2820 45%,#171513 100%)}
.why-person{left:720px;top:1673px;width:380px;height:461px;background:linear-gradient(180deg,#3a2a20 0%,#c9a38a 40%,#f2efeb 75%,#e6e3df 100%);border-radius:190px 190px 0 0;opacity:.9}
.why-content{left:0;top:1673px;width:1200px;height:461px}
.why-content h2{position:absolute;left:61px;top:86px;color:var(--white);font-size:33px;font-weight:700;line-height:44px;text-transform:uppercase}
.why-content ul{position:absolute;left:61px;top:190px;list-style:none;width:540px}
.why-content li{color:var(--white);font-size:15px;line-height:26px;padding-left:28px;position:relative;margin-bottom:6px}
.why-content li svg{position:absolute;left:0;top:6px}
.btn-catalog{left:61px;top:329px;width:192px;height:44px;line-height:40px;text-align:center;font-size:15px;position:absolute}

/* products */
.products{left:0;top:2134px;width:1200px;height:676px;background:var(--grey)}
.products h2{position:absolute;left:0;top:102px;width:1200px;text-align:center;font-family:"Krona One",sans-serif;font-size:38px;font-weight:400;color:var(--ink)}
.card{position:absolute;top:223px;width:250px;height:366px;background:var(--white)}
.card .title{position:absolute;left:14px;top:12px;font-size:15px;font-weight:700;color:var(--ink)}
.card .price{position:absolute;left:14px;top:38px;font-size:14px;font-weight:700;color:var(--ink)}
.card .price s{color:#999;font-weight:400;margin-right:4px}
.card .stars{position:absolute;left:14px;top:60px;color:var(--star);font-size:11px;letter-spacing:1px}
.card .sale{position:absolute;right:0;top:58px;background:var(--sale);color:var(--white);font-size:11px;font-weight:700;padding:3px 8px 3px 14px;clip-path:polygon(10px 0,100% 0,100% 100%,10px 100%,0 50%)}
.card .tools{position:absolute;right:6px;top:98px;display:flex;flex-direction:column;gap:4px}
.card .tools span{width:30px;height:30px;background:var(--olive);display:flex;align-items:center;justify-content:center}
.card .tools span.dark{background:var(--ink)}
.card .photo{position:absolute;left:40px;top:110px;width:170px;height:140px;border-radius:8px}
.card .name{position:absolute;left:0;top:285px;width:250px;text-align:center;font-size:15px;font-weight:600;color:var(--ink)}
.card .add{position:absolute;left:68px;top:314px;width:114px;height:40px;line-height:36px;text-align:center;font-size:16px;border-radius:3px}
.arrow{position:absolute;top:395px}

/* delivery */
.delivery{left:0;top:2810px;width:1200px;height:100px;background:var(--olive)}
.delivery .item{position:absolute;top:0;height:100px;display:flex;align-items:center;gap:22px;color:var(--white)}
.delivery h5{font-size:18px;font-weight:700;text-transform:uppercase}
.delivery p{font-size:14px}

/* footer */
.footer{left:0;top:2910px;width:1200px;height:357px}
.footer h6{position:absolute;top:76px;font-size:19px;font-weight:700;color:var(--ink);text-transform:uppercase}
.contact-row{position:absolute;left:61px;display:flex;gap:20px;font-size:13px;line-height:22px;color:var(--ink)}
.links{position:absolute;left:381px;top:121px;list-style:none}
.links li{font-size:13px;line-height:24px;color:var(--ink);padding-left:14px;position:relative}
.links li:before{content:"";position:absolute;left:2px;top:10px;width:4px;height:4px;border-radius:50%;background:var(--ink)}
.pay{position:absolute;display:flex;gap:10px}
.pay span{height:24px;border-radius:3px}
.sub{position:absolute;left:577px;top:178px;font-size:12px;font-weight:700;color:var(--ink);text-transform:uppercase}
.news-copy{position:absolute;left:882px;top:126px;width:300px;font-size:13px;line-height:24px;color:var(--ink)}
.news-form{position:absolute;left:882px;top:184px;width:264px;height:36px;display:flex;border:1px solid #bbb}
.news-form .field{flex:1;font-size:12px;padding:9px 10px;color:var(--ink)}
.news-form .go{width:52px;background:var(--ink);display:flex;align-items:center;justify-content:center}
.news-social{position:absolute;left:882px;top:240px;display:flex;gap:14px}
.news-social span{width:12px;height:12px;border-radius:50%;background:#999}
.legal{position:absolute;left:61px;top:320px;width:1078px;border-top:1px solid #bbb;padding-top:12px;display:flex;justify-content:space-between;font-size:12px;color:var(--ink)}
.legal nav{display:flex;gap:26px}
</style>
</head>
<body>

<header class="abs topbar">
  <div class="abs brand"><span class="mark"></span><span>VELMI Sàrl</span></div>
  <div class="abs callus">CALL US NOW
    <svg width="22" height="22" viewBox="0 0 24 24"><path d="M6.6 10.8a15 15 0 006.6 6.6l2.2-2.2a1 1 0 011-.25 11.4 11.4 0 003.6.57 1 1 0 011 1V20a1 1 0 01-1 1A17 17 0 013 4a1 1 0 011-1h3.5a1 1 0 011 1c0 1.25.2 2.45.57 3.57a1 1 0 01-.25 1z" fill="#a59a4c"/></svg>
    <span>+41 21 555 0190</span></div>
  <div class="abs social"><span></span><span></span><span></span></div>
  <div class="abs search">
    <div class="field">Search</div>
    <div class="cat">All Categories</div>
    <div class="go"><svg width="20" height="20" viewBox="0 0 24 24"><circle cx="10" cy="10" r="6.5" fill="none" stroke="#fff" stroke-width="2.6"/><path d="M15 15l6 6" stroke="#fff" stroke-width="3"/></svg></div>
  </div>
  <div class="abs cart">My Cart
    <svg width="32" height="28" viewBox="0 0 32 28"><path d="M1 2h5l4 15h16l4-11H8" fill="none" stroke="#1f1f1f" stroke-width="3"/><path d="M9 6h21l-4 11H11z" fill="#1f1f1f"/><circle cx="12" cy="24" r="2.5" fill="#1f1f1f"/><circle cx="24" cy="24" r="2.5" fill="#1f1f1f"/></svg>
    <span class="count">0</span></div>
</header>

<nav class="abs nav">
  <a class="active" href="#" style="left:61px">Home</a>
  <a href="#" style="left:159px">Services</a>
  <a href="#" style="left:279px">Products</a>
  <a href="#" style="left:407px">Example</a>
  <a href="#" style="left:523px">Download</a>
  <a href="#" style="left:662px">Contacts</a>
</nav>

<section class="abs hero" role="img" aria-label="Photo of an engineer testing a car engine with a multimeter next to a laptop showing a chart"></section>
<div class="abs hero-title">
  <div class="l1">CONCEPT AND DESIGN OF ELECTRONIC</div>
  <div class="l2">CIRCUITS AND MECHANICAL UNITS</div>
</div>

<section class="abs promo">
  <svg class="abs bg" width="1200" height="172" viewBox="0 0 1200 172"><rect width="1200" height="172" fill="#242424"/><polygon points="0,0 642,0 588,172 0,172" fill="#a59a4c"/></svg>
  <svg class="abs" style="left:61px;top:38px" width="124" height="96" viewBox="0 0 124 96"><path d="M30 90a28 28 0 01-2-56 34 34 0 0164-6 26 26 0 012 62z" fill="#fff"/><path d="M62 34v34M48 54l14 16 14-16" fill="none" stroke="#a59a4c" stroke-width="9"/></svg>
  <h3 style="left:207px;top:38px">Download Notes and Brochers</h3>
  <p style="left:207px;top:76px">By choosing VELMI Ltd., you can get the most from your product. We provide you with new and innovative solutions that allow you to optimize</p>
  <svg class="abs" style="left:632px;top:44px" width="136" height="86" viewBox="0 0 136 86"><g fill="#fff"><circle cx="22" cy="44" r="15"/><rect x="15" y="60" width="14" height="14"/><circle cx="62" cy="34" r="20"/><rect x="53" y="56" width="18" height="18"/><circle cx="110" cy="24" r="24"/><rect x="99" y="50" width="22" height="22"/></g></svg>
  <h3 style="left:788px;top:38px">Check Out Examples</h3>
  <p style="left:788px;top:76px">By choosing VELMI Ltd., you can get the most from your product. We provide you with new and innovative solutions that allow you to optimize</p>
</section>

<h1 class="abs welcome-title">WELCOME TO <span class="name">VELMI</span></h1>
<p class="abs intro">The ever-increasing complexity in modern systems, the search for reliability and performance and the continuous desire to reduce production costs and dimensions of the products require a rigorous integration between the electronic units, software and mechanical systems.<br>VELMI Ltd. designs systems in which electronics, software and mechanics are perfectly integrated</p>

<div class="abs feature" style="left:39px;top:1218px">
  <svg width="100" height="100" viewBox="0 0 100 100"><rect x="8" y="26" width="66" height="48" rx="3" fill="none" stroke="#1f1f1f" stroke-width="7"/><rect x="30" y="74" width="22" height="10" fill="#1f1f1f"/><rect x="22" y="84" width="38" height="6" fill="#1f1f1f"/><circle cx="72" cy="24" r="14" fill="none" stroke="#a59a4c" stroke-width="9" stroke-dasharray="6 4"/><circle cx="72" cy="24" r="6" fill="#a59a4c"/></svg>
  <h4>Software</h4>
  <p>Through a multi-physics modelling approach, Velmi Ltd. can integrate into the simulation</p>
</div>
<div class="abs feature" style="left:326px;top:1218px">
  <svg width="110" height="100" viewBox="0 0 110 100"><circle cx="20" cy="20" r="8" fill="#1f1f1f"/><path d="M12 32h16v62h-6V62h-4v32h-6z" fill="#1f1f1f"/><path d="M28 40l16-6" stroke="#1f1f1f" stroke-width="5"/><rect x="40" y="24" width="64" height="46" rx="4" fill="#a59a4c"/><rect x="56" y="48" width="8" height="14" fill="#fff"/><rect x="70" y="40" width="8" height="22" fill="#fff"/><rect x="84" y="32" width="8" height="30" fill="#fff"/></svg>
  <h4>Simulation and Modeling</h4>
  <p>Through a multi-physics modelling approach, Velmi Ltd. can integrate into the simulation</p>
</div>
<div class="abs feature" style="left:600px;top:1218px">
  <svg width="100" height="100" viewBox="0 0 100 100"><circle cx="50" cy="50" r="34" fill="none" stroke="#1f1f1f" stroke-width="12" stroke-dasharray="10 7"/><circle cx="50" cy="50" r="26" fill="#1f1f1f"/><rect x="36" y="36" width="28" height="28" fill="#a59a4c"/><rect x="43" y="43" width="14" height="14" fill="#1f1f1f"/></svg>
  <h4>Mechanics</h4>
  <p>Through a multi-physics modelling approach, Velmi Ltd. can integrate into the simulation</p>
</div>
<div class="abs feature" style="left:883px;top:1218px">
  <svg width="100" height="100" viewBox="0 0 100 100"><circle cx="50" cy="50" r="36" fill="none" stroke="#1f1f1f" stroke-width="12" stroke-dasharray="11 6"/><circle cx="50" cy="50" r="28" fill="#1f1f1f"/><circle cx="50" cy="44" r="13" fill="#a59a4c"/><rect x="44" y="56" width="12" height="12" fill="#a59a4c"/></svg>
  <h4>Electronics</h4>
  <p>Through a multi-physics modelling approach, Velmi Ltd. can integrate into the simulation</p>
</div>
<a class="abs btn btn-services" href="#">View Our Services</a>

<section class="abs why" role="img" aria-label="Dark background of mechanical gears"></section>
<div class="abs why-person" role="img" aria-label="Photo of a smiling customer support agent wearing a headset"></div>
<section class="abs why-content">
  <h2>Why are we the best products<br>and lifestyle store</h2>
  <ul>
    <li><svg width="16" height="14" viewBox="0 0 16 14"><path d="M1 7l5 5 9-11" fill="none" stroke="#d9c862" stroke-width="3"/></svg>Over 23 passionate full time staff.</li>
    <li><svg width="16" height="14" viewBox="0 0 16 14"><path d="M1 7l5 5 9-11" fill="none" stroke="#d9c862" stroke-width="3"/></svg>Over 17 physical store locations (and growing!).</li>
    <li><svg width="16" height="14" viewBox="0 0 16 14"><path d="M1 7l5 5 9-11" fill="none" stroke="#d9c862" stroke-width="3"/></svg>Free shipping on all supplement orders, every day to anywhere in Australia!</li>
  </ul>
  <a class="btn btn-catalog" href="#">Download ECatalog</a>
</section>

<section class="abs products">
  <h2>VIEW SOME FEATURED PRODUCTS</h2>
  <svg class="arrow" style="left:22px" width="20" height="36" viewBox="0 0 20 36"><path d="M17 2L3 18l14 16" fill="none" stroke="#1f1f1f" stroke-width="4"/></svg>
  <svg class="arrow" style="left:1160px" width="20" height="36" viewBox="0 0 20 36"><path d="M3 2l14 16L3 34" fill="none" stroke="#1f1f1f" stroke-width="4"/></svg>

  <article class="card" style="left:59px">
    <div class="title">Cat5E Flex Patch Cords</div>
    <div class="price"><s>$120.00</s>$110.00</div>
    <div class="stars">★★★★★</div>
    <div class="sale">SALE</div>
    <div class="tools"><span><svg width="14" height="14" viewBox="0 0 24 24"><circle cx="10" cy="10" r="7" fill="none" stroke="#fff" stroke-width="3"/><path d="M15 15l7 7" stroke="#fff" stroke-width="3"/></svg></span><span class="dark"><svg width="14" height="14" viewBox="0 0 24 24"><path d="M12 21L3 12a5 5 0 019-6 5 5 0 019 6z" fill="#fff"/></svg></span></div>
    <div class="photo" role="img" aria-label="Product photo of a black stepper motor unit" style="background:radial-gradient(circle,#6b6b6b,#1e1e1e 60%,#fff 72%)"></div>
    <div class="name">Cat5E Flex Patch Cords</div>
    <a class="btn add" href="#">Add to Cart</a>
  </article>
  <article class="card" style="left:335px">
    <div class="title">Cat5E Flex Patch Cords</div>
    <div class="price"><s>$120.00</s>$110.00</div>
    <div class="stars">★★★★★</div>
    <div class="tools"><span><svg width="14" height="14" viewBox="0 0 24 24"><circle cx="10" cy="10" r="7" fill="none" stroke="#fff" stroke-width="3"/><path d="M15 15l7 7" stroke="#fff" stroke-width="3"/></svg></span><span class="dark"><svg width="14" height="14" viewBox="0 0 24 24"><path d="M12 21L3 12a5 5 0 019-6 5 5 0 019 6z" fill="#fff"/></svg></span></div>
    <div class="photo" role="img" aria-label="Product photo of a servo motor" style="background:radial-gradient(circle,#8a8a8a,#2a2a2a 60%,#fff 72%)"></div>
    <div class="name">Cat5E Flex Patch Cords</div>
    <a class="btn add" href="#">Add to Cart</a>
  </article>
  <article class="card" style="left:612px">
    <div class="title">Cat5E Flex Patch Cords</div>
    <div class="price"><s>$120.00</s>$110.00</div>
    <div class="stars">★★★★★</div>
    <div class="photo" role="img" aria-label="Product photo of a green circuit board" style="background:radial-gradient(circle,#3f8a4a,#1d4a26 60%,#fff 72%)"></div>
    <div class="name">Cat5E Flex Patch Cords</div>
    <a class="btn add" href="#">Add to Cart</a>
  </article>
  <article class="card" style="left:889px">
    <div class="title">Cat5E Flex Patch Cords</div>
    <div class="price"><s>$120.00</s>$110.00</div>
    <div class="stars">★★★★★</div>
    <div class="sale">SALE</div>
    <div class="tools"><span><svg width="14" height="14" viewBox="0 0 24 24"><circle cx="10" cy="10" r="7" fill="none" stroke="#fff" stroke-width="3"/><path d="M15 15l7 7" stroke="#fff" stroke-width="3"/></svg></span><span class="dark"><svg width="14" height="14" viewBox="0 0 24 24"><path d="M12 21L3 12a5 5 0 019-6 5 5 0 019 6z" fill="#fff"/></svg></span></div>
    <div class="photo" role="img" aria-label="Product photo of a starter motor" style="background:radial-gradient(circle,#c9b98a,#6b5f3f 60%,#fff 72%)"></div>
    <div class="name">Cat5E Flex Patch Cords</div>
    <a class="btn add" href="#">Add to Cart</a>
  </article>
</section>

<section class="abs delivery">
  <svg class="abs" style="left:0;top:0" width="460" height="100" viewBox="0 0 460 100"><polygon points="0,0 460,0 425,100 0,100" fill="#242424"/></svg>
  <svg class="abs" style="left:835px;top:0" width="40" height="100" viewBox="0 0 40 100"><path d="M36 0L4 100" stroke="#8c8240" stroke-width="3"/></svg>
  <div class="item" style="left:66px">
    <svg width="56" height="56" viewBox="0 0 56 56"><circle cx="28" cy="28" r="26" fill="#fff"/><path d="M12 20c6 0 8 4 12 4s2 8 8 8-2 8 2 12M34 8c-2 6 4 8 8 8s6 4 10 4" fill="none" stroke="#242424" stroke-width="4"/></svg>
    <div><h5>International Delivery</h5><p>Over 20 Countries</p></div>
  </div>
  <div class="item" style="left:470px">
    <svg width="50" height="60" viewBox="0 0 50 60"><rect x="5" y="4" width="40" height="52" rx="20" fill="none" stroke="#fff" stroke-width="5"/><path d="M25 6v18M6 26h38" stroke="#fff" stroke-width="4"/></svg>
    <div><h5>Click &amp; Collect</h5><p>Consectetur Adipiscing Elit</p></div>
  </div>
  <div class="item" style="left:790px">
    <svg width="76" height="56" viewBox="0 0 76 56"><path d="M6 36V26l10-16h40l12 16v10z" fill="#fff"/><rect x="22" y="14" width="14" height="12" fill="#a59a4c"/><rect x="40" y="14" width="14" height="12" fill="#a59a4c"/><circle cx="20" cy="40" r="8" fill="#fff" stroke="#a59a4c" stroke-width="3"/><circle cx="56" cy="40" r="8" fill="#fff" stroke="#a59a4c" stroke-width="3"/></svg>
    <div><h5>Free Standard Delivery</h5><p>Orders $50 and over</p></div>
  </div>
</section>

<footer class="abs footer">
  <h6 style="left:61px">Contact Us</h6>
  <div class="contact-row" style="top:128px">
    <svg width="16" height="16" viewBox="0 0 16 16" style="margin-top:4px"><path d="M2 8l6-6 6 6v7H2z" fill="none" stroke="#777" stroke-width="1.5"/></svg>
    <span>48 Rue des Artisans Lausanne,<br>Switzerland</span></div>
  <div class="contact-row" style="top:190px">
    <svg width="16" height="16" viewBox="0 0 16 16" style="margin-top:4px"><rect x="4" y="1" width="8" height="14" rx="1" fill="none" stroke="#777" stroke-width="1.5"/></svg>
    <span>+41 21 555 0191</span></div>
  <div class="contact-row" style="top:230px">
    <svg width="16" height="16" viewBox="0 0 16 16" style="margin-top:4px"><rect x="1" y="3" width="14" height="10" fill="none" stroke="#777" stroke-width="1.5"/><path d="M1 3l7 6 7-6" fill="none" stroke="#777" stroke-width="1.5"/></svg>
    <span>contact@velmi-example.ch</span></div>

  <h6 style="left:381px">Services</h6>
  <ul class="links">
    <li>About Us</li><li>Privacy Policy</li><li>Terms &amp; Condition</li><li>Best Seller</li><li>Manufactures</li>
  </ul>

  <h6 style="left:577px">Payment Methods</h6>
  <div class="pay" style="left:577px;top:124px"><span style="width:40px;background:#e9e9e9"></span><span style="width:48px;background:#e9e9e9;border-radius:12px"></span><span style="width:36px;background:#e9e9e9"></span><span style="width:40px;background:#e9e9e9"></span></div>
  <div class="sub">Shipping Partner</div>
  <div class="pay" style="left:577px;top:206px"><span style="width:24px;background:#e2e2e2"></span><span style="width:40px;background:#e2e2e2"></span><span style="width:40px;background:#e2e2e2"></span><span style="width:40px;background:#e2e2e2"></span></div>
  <div class="pay" style="left:585px;top:240px"><span style="width:40px;background:#e2e2e2"></span><span style="width:40px;background:#e2e2e2"></span><span style="width:36px;background:#e2e2e2"></span></div>

  <h6 style="left:882px">Newsletter !</h6>
  <p class="news-copy">Sign up for our newsletter and get 15% off your next order.</p>
  <div class="news-form"><div class="field">Enter your email here*</div><div class="go"><svg width="18" height="4" viewBox="0 0 18 4"><rect width="18" height="3" fill="#fff"/></svg></div></div>
  <div class="news-social"><span></span><span></span><span></span><span></span><span></span></div>

  <div class="legal">
    <span>© 2016 Copyright VELMI SÀRL All Right Reserved.</span>
    <nav><span>Privacy &amp; Cookies</span><span>Terms &amp; Conditions</span><span>Accessibility</span><span>Store Directory</span><span>About Us</span></nav>
  </div>
</footer>

</body>
</html>
```